yourSmileCare Brookvale Business Card

Please design a two sided business card that is Elegant and Professional
Add subtle elegant patterns to suit Spot UV printing/ or raised printing

Name: Dr Marcus T. Fenwick
Qualification: BDSc (QLD)
Title: Dental Surgeon, Clinical Director
Company: yourSmileCare Brookvale
Phone: (02) 7593 2268
Address: Shop 7/18-20 Lindon Ave Brookvale 2097
email: info@yoursmilecarebrookvale.com.au
Facebook: friendnet.com/yoursmilecarebrookvale

Motto:
Quality dentistry you can trust

Description of services (not compulsory):
Preventative Dentistry | General Dentistry
Cosmetic Dentistry | Teeth Whitening
Crown and Bridge | Root Canal Therapy
Veneers | Clearvono | Orthodontics
Emergency Dental Care | After Hours

Personalised Treatment Plans
Transparent Fees

Please make sure card is elegant and professional

Target Market(s)

general population, patients,
Dental sales companies, other professions

Industry/Entity Type

Dental Clinic

Contact Information for Business Card

Name: Dr Marcus T. Fenwick
Qualification: BDSc (QLD)
Phone: (02) 7593 2268
Address: Shop 7/18-20 Lindon Ave Brookvale

Motto:

Description of services (not compulsory)

Transparent Fees

Image of dental surgery optional

Please make sure card is elegant and profession

Requirements
Must have
• Logo
• Name, Title (next to name), Business
• Phone, address, facbeook
• Must have stylish design to suit SPOT UV reflective printing
Nice to have
• Subtle elegant patterns which will have Spot UV on them when printed
• Colours to match logo colour
• Description of services
Should not have
• Small fonts that are hard to read
• DO NOT PUT IMAGES OF DENTAL INSTRUMENTS OR TEETH PLEASE

```html
<!DOCTYPE html>
<html lang="en">
<head>
<meta charset="utf-8">
<title>yourSmileCare Brookvale Business Card</title>
<link href="https://fonts.googleapis.com/css2?family=Montserrat:wght@400;500;600;700&display=swap" rel="stylesheet">
<style>
  :root {
    --backdrop: #d9d9d6;
    --green: #7cc242;
    --slate: #7a7a78;
    --cream: #efeee6;
    --white: #ffffff;
    --ink-soft: #f2f2f0;
  }
  * { box-sizing: border-box; margin: 0; padding: 0; }
  html, body { width: 1200px; height: 786px; overflow: hidden; }
  body {
    background: var(--backdrop);
    font-family: "Montserrat", sans-serif;
    display: flex;
    align-items: center;
    justify-content: center;
    gap: 40px;
  }
  .card {
    position: relative;
    width: 520px;
    height: 297px;
    border-radius: 16px;
    overflow: hidden;
    box-shadow: 0 10px 24px rgba(0,0,0,0.18);
  }
  .card-art { position: absolute; inset: 0; }

  /* Front */
  .front .identity {
    position: absolute;
    left: 30px;
    top: 30px;
    color: var(--white);
  }
  .doctor-name {
    font-size: 15px;
    font-weight: 700;
    letter-spacing: 0.3px;
    text-transform: uppercase;
  }
  .doctor-name .qual { font-weight: 500; text-transform: none; font-size: 12px; }
  .doctor-title { font-size: 11.5px; font-weight: 400; margin-top: 4px; }
  .address { font-size: 11.5px; line-height: 1.45; margin-top: 22px; }
  .contact-list {
    list-style: none;
    position: absolute;
    left: 30px;
    top: 170px;
    color: var(--white);
    font-size: 11.5px;
  }
  .contact-list li {
    display: flex;
    align-items: center;
    gap: 8px;
    height: 21px;
  }
  .contact-icon { width: 14px; height: 14px; flex: none; }
  .front .brand {
    position: absolute;
    right: 28px;
    bottom: 46px;
    display: flex;
    align-items: center;
    gap: 8px;
  }
  .brand-dot {
    width: 12px; height: 12px; border-radius: 50%;
    background: var(--green);
  }
  .brand-name {
    font-size: 21px;
    font-weight: 600;
    color: var(--green);
    line-height: 1.1;
    text-align: left;
  }

  /* Back */
  .back { background: var(--slate); color: var(--ink-soft); }
  .back .brand {
    position: absolute;
    left: 0; right: 0;
    top: 62px;
    display: flex;
    justify-content: center;
    align-items: center;
    gap: 10px;
  }
  .back .brand-name { color: var(--white); font-size: 26px; }
  .back .brand-dot { background: var(--white); width: 14px; height: 14px; }
  .services {
    position: absolute;
    left: 0; right: 0;
    top: 150px;
    text-align: center;
    font-size: 11px;
    line-height: 1.6;
    font-weight: 500;
  }
  .services .sep { color: var(--green); font-weight: 700; padding: 0 3px; }
  .website {
    position: absolute;
    left: 0; right: 0;
    bottom: 26px;
    text-align: center;
    font-size: 12px;
    font-weight: 600;
    color: var(--white);
  }
  .website .domain { color: var(--green); }
</style>
</head>
<body>

<section class="card front" aria-label="Business card front">
  <svg class="card-art" viewBox="0 0 520 297" preserveAspectRatio="none" aria-hidden="true">
    <rect width="520" height="297" fill="var(--green)"/>
    <path d="M395 0 C300 70 250 170 236 297 L520 297 L520 0 Z" fill="var(--slate)"/>
    <path d="M520 14 C400 40 300 140 268 297 L520 297 Z" fill="var(--cream)"/>
  </svg>

  <div class="identity">
    <p class="doctor-name">Dr Marcus T. Fenwick <span class="qual">BDSc (QLD)</span></p>
    <p class="doctor-title">Dental Surgeon, Clinical Director</p>
    <p class="address">Shop 7/18-20 Lindon Ave<br>Brookvale 2097</p>
  </div>

  <ul class="contact-list">
    <li>
      <svg class="contact-icon" viewBox="0 0 14 14" aria-hidden="true">
        <rect width="14" height="14" rx="3" fill="var(--white)"/>
        <path d="M4 3.5 L5.6 3.5 L6.2 5.6 L5.2 6.4 C5.7 7.6 6.5 8.4 7.6 8.9 L8.4 7.9 L10.5 8.5 L10.5 10.1 C7 10.3 3.8 7.1 4 3.5 Z" fill="var(--green)"/>
      </svg>
      (02) 7593 2268
    </li>
    <li>
      <svg class="contact-icon" viewBox="0 0 14 14" aria-hidden="true">
        <rect width="14" height="14" rx="3" fill="var(--white)"/>
      </svg>
      friendnet.com/yoursmilecarebrookvale
    </li>
    <li>
      <svg class="contact-icon" viewBox="0 0 14 14" aria-hidden="true">
        <rect width="14" height="14" rx="3" fill="var(--white)"/>
        <rect x="3" y="4.2" width="8" height="5.6" fill="none" stroke="var(--green)" stroke-width="1"/>
        <path d="M3 4.2 L7 7.4 L11 4.2" fill="none" stroke="var(--green)" stroke-width="1"/>
      </svg>
      info@yoursmilecarebrookvale.com.au
    </li>
    <li>
      <svg class="contact-icon" viewBox="0 0 14 14" aria-hidden="true">
        <rect width="14" height="14" rx="3" fill="var(--white)"/>
        <circle cx="7" cy="7" r="3.8" fill="none" stroke="var(--green)" stroke-width="1"/>
        <path d="M3.2 7 H10.8 M7 3.2 C5.4 5 5.4 9 7 10.8 M7 3.2 C8.6 5 8.6 9 7 10.8" fill="none" stroke="var(--green)" stroke-width="0.9"/>
      </svg>
      www.yoursmilecarebrookvale.com.au
    </li>
  </ul>

  <div class="brand">
    <span class="brand-dot" aria-hidden="true"></span>
    <p class="brand-name">yourSmileCare<br>Brookvale</p>
  </div>
</section>

<section class="card back" aria-label="Business card back">
  <div class="brand">
    <span class="brand-dot" aria-hidden="true"></span>
    <p class="brand-name">yourSmileCare Brookvale</p>
  </div>

  <div class="services">
    <p>Preventative Dentistry<span class="sep">•</span>General Dentistry<span class="sep">•</span>Cosmetic Dentistry<span class="sep">•</span>Teeth Whitening</p>
    <p>Crown and Bridge<span class="sep">•</span>Root Canal Therapy<span class="sep">•</span>Veneers<span class="sep">•</span>Clearvono<span class="sep">•</span>Orthodontics</p>
    <p>Emergency Dental Care<span class="sep">•</span>After Hours</p>
    <p>Personalised Treatment Plans<span class="sep">•</span>Transparent Fees</p>
  </div>

  <p class="website">www.<span class="domain">yoursmilecarebrookvale</span>.com.au</p>
</section>

</body>
</html>
```